イベントの雰囲気を伝え、集客に効果のあるイベントバナーデザインを募集! 継続発注あり!1採用5,000円! この秋から開講する生産者から農業の最前線を学ぶ「ノルカビジネススクール」のイベントページに掲載するバナー画像の作成のご依頼です。 ノルカビジネススクールは、新規就農者向けの講座で、東京で開催されます。2016年も開催され、累計500名以上の参加者が集った人気講座となっております。 今年も開講するにあたり、イベントの看板となるようなカバー画像の作成をお願い致します。 【依頼内容】 イベントページ(Qumvo、Lintroom)のカバー画像の作成依頼です。 後述のように、毎月開催する予定ですので、ゲストの顔画像などを変えることで、毎月共通して使えるような、講座のシンボルとなるような画像をお願いいたします。 たくさんのデザイナーさんからのご提案をお待ちしております。 <ノルカビジネススクールとは?> ノルカビジネススクールは、「農業するなら宮崎」をキーワードに、新規就農を促進する目的で展開されている宮崎県の新規就農講座です。東京で開催され、毎回宮崎県から、テーマに沿ったゲスト(農家の方や農業ビジネス従事者)を迎え、農業の魅力を語り、学ぶ場です。 開催頻度は、月に2回〜3回で、就農希望者はもちろん、移住希望者や、地域ビジネスを学びたいという方まで、幅広く参加いただいています。 ■納品形式: 716px×400pxのサイズでの製作をお願いします。jpeg または pngを希望します。 合わせて、aiまたはPSDデータも合わせていただけますと幸いです。 ■使用意図: イベントページ(Qumvo、Lintroom)のカバー画像として仕様いたします。スマートフォン環境でも、PC環境でも強い訴求力を持たせて、集客に結びつけたいと考えております。 またイベント告知の記事などをWEBで配信する際に、そちらにも活用させていただく予定です。 ■参考イメージ: イメージは、このような感じかと思います。 https://velmora-course.jp/ このページのTOP画像のように、「社会人向け農業ビジネス講座」であるということがわかるのが良いと考えています。 農業というと、野菜のイメージになりがちなのですが、野菜というイメージよりも、例えば下記のように、 http://qumvo.com/event/583120?lang=ja 青空と畑というところに、講座名と、農業に関する要素が入るのが良いのではないかと考えています。 デザインの品質としては、イベント内容を表すような形で、連動性が優れ、印象に残るものができればと考えております。 <加えたい内容> 画像内には、例えば、 - 講座名 - 登壇者の顔(イベント毎に変更) - 場所/時間(イベント毎に変更) こちらは最低限かなと考えております。 ※製作時は、上記の要素をダミーで当て込んてください。 ※ゲストは、多くの場合1人を予定していますが、3人まで表示できますと幸いです。 ■目指す成果/目的 このカバー画像を見て、「気になる」と思い、イベントの詳細をクリックしていただくことが目的です。 ■ターゲット 20歳〜40歳くらいの男女、地域に関する情報に感度が高く、移住などにも関心がある。 キーワードとしては、 新規就農、地域ビジネス、半農半X、移住、農業ビジネスなどが挙げられます。 ■スケジュール 8月2日いっぱいでのご提案 ※納品:8月3日を想定 ※タイトな納期で申し訳ありません。こちらご相談させていただくことも可能です。 ■費用 5000円を想定しております。 【選定基準・注意事項】 ・継続的に特産品の販売に取り組めるデザイナーさんを探しています。 ・採用されたバナーに対して、修正・変更を加えさせて頂き、展開する場合がございます。予めご了承下さい。 ・他で登録されているデザインや商標の転用など、他社の知的財産権を侵すことの無いようお願いします。 たくさんのデザイナーさんからのご提案をお待ちしております。 |

```html
<!DOCTYPE html>
<html lang="ja">
<head>
<meta charset="utf-8">
<title>農業するなら宮崎 | ノルカビジネススクール</title>
<link rel="stylesheet" href="https://fonts.googleapis.com/css2?family=Noto+Sans+JP:wght@500;700;900&family=Shippori+Mincho:wght@500;600&display=swap">
<style>
  :root {
    --sky-top: #5d9fd6;
    --sky-mid: #b9d7ea;
    --hill: #5f8c52;
    --field: #7fae4a;
    --field-deep: #3f6b2c;
    --white: #ffffff;
    --ink: #1e2420;
    --badge: #f6d21c;
    --badge-red: #d6261b;
    --bar: rgba(20, 40, 25, 0.45);
    --face: #c9a98b;
  }
  * { margin: 0; padding: 0; box-sizing: border-box; }
  html, body { width: 1200px; height: 670px; overflow: hidden; background: #fff; }
  .banner {
    position: relative;
    width: 1200px;
    height: 670px;
    overflow: hidden;
    font-family: "Noto Sans JP", sans-serif;
  }
  .landscape {
    position: absolute; inset: 0;
    background: linear-gradient(180deg, var(--sky-top) 0%, var(--sky-mid) 30%, #9dbf9a 42%, var(--hill) 55%, var(--field) 72%, var(--field-deep) 100%);
  }
  .region-area {
    position: absolute;
    left: 420px; top: 0; width: 560px; height: 670px;
    background: radial-gradient(ellipse at 55% 50%, rgba(255,255,255,0.28) 0%, rgba(255,255,255,0.12) 45%, rgba(255,255,255,0) 72%);
  }
  .info-label {
    position: absolute; left: 20px; width: 470px; height: 36px;
    border: 2px solid var(--white);
    background: rgba(255,255,255,0.12);
    color: var(--white);
    font-size: 20px; font-weight: 700;
    display: flex; align-items: center; justify-content: center;
    text-shadow: 0 0 6px rgba(0,0,0,0.5);
  }
  .info-text {
    position: absolute; left: 20px; width: 470px;
    text-align: center;
    color: var(--white);
    font-weight: 900;
    line-height: 1.2;
    text-shadow: 0 0 6px rgba(0,0,0,0.7), 0 2px 4px rgba(0,0,0,0.6);
  }
  .course-name { top: 76px; font-size: 24px; }
  .venue { top: 388px; font-size: 24px; }
  .date { top: 512px; font-size: 26px; }
  .guests { position: absolute; left: 20px; top: 138px; width: 470px; height: 146px; }
  .guest {
    position: absolute; top: 0; width: 142px; height: 142px; border-radius: 50%;
    border: 4px solid var(--white);
    background: radial-gradient(circle at 50% 40%, #e6d2bd, var(--face) 60%, #7d9c68);
  }
  .guest:nth-child(1) { left: 4px; }
  .guest:nth-child(2) { left: 164px; }
  .guest:nth-child(3) { left: 324px; }
  .headline-small {
    position: absolute; left: 1016px; top: 64px;
    writing-mode: vertical-rl;
    font-family: "Shippori Mincho", serif;
    font-size: 64px; font-weight: 600; color: var(--ink);
    line-height: 1; letter-spacing: 2px;
  }
  .headline-large {
    position: absolute; left: 800px; top: 180px;
    writing-mode: vertical-rl;
    font-family: "Shippori Mincho", serif;
    font-size: 190px; font-weight: 500; color: var(--ink);
    line-height: 1; letter-spacing: -6px;
  }
  .badge {
    position: absolute; left: 856px; top: 10px; width: 144px; height: 144px; border-radius: 50%;
    background: var(--badge);
    display: flex; flex-direction: column; align-items: center; justify-content: center;
    color: var(--ink); font-weight: 900; line-height: 1.1; font-size: 18px; text-align: center;
  }
  .badge .count { color: var(--badge-red); font-size: 32px; }
  .footer-bar {
    position: absolute; left: 0; bottom: 0; width: 1200px; height: 50px;
    background: var(--bar);
    color: var(--white); font-size: 22px; font-weight: 500;
  }
  .footer-bar span { position: absolute; top: 50%; transform: translate(-50%, -50%); white-space: nowrap; }
  .footer-bar .school { left: 290px; }
  .footer-bar .tagline { left: 950px; }
</style>
</head>
<body>
<div class="banner">
  <div class="landscape" role="img" aria-label="青空の下に広がる山あいの棚田と畑の風景"></div>
  <div class="region-area" role="img" aria-label="宮崎県の地図シルエットが半透明で入る領域"></div>

  <div class="info-label" style="top:20px">講座名</div>
  <p class="info-text course-name">新規就農者向け宮崎で農業をしたい!!</p>

  <div class="guests">
    <div class="guest" role="img" aria-label="ゲスト登壇者1の顔写真"></div>
    <div class="guest" role="img" aria-label="ゲスト登壇者2の顔写真"></div>
    <div class="guest" role="img" aria-label="ゲスト登壇者3の顔写真"></div>
  </div>

  <div class="info-label" style="top:340px">場所</div>
  <p class="info-text venue">東京ミナトシティ ルミナホール</p>

  <div class="info-label" style="top:446px">日時</div>
  <p class="info-text date">2017年11月11日(土)12時〜</p>

  <div class="badge">
    <span>2016年</span>
    <span>参加者</span>
    <span>累計</span>
    <span class="count">500名</span>
    <span>以上</span>
  </div>

  <h1 class="headline-small">農業するなら</h1>
  <div class="headline-large">宮崎</div>

  <div class="footer-bar">
    <span class="school">ノルカビジネススクール</span>
    <span class="tagline">社会人向け農業ビジネス講座</span>
  </div>
</div>
</body>
</html>
```